Relationship Seminar

I am an Author and Speaker and I need a flyer for a Christian relationship seminar targeting women aged between mid 20's to late 30's. It's an event for women only.

-I am looking for a fresh/ edgy look but still feminine
-Nothing too girly
-Maximum of 3 colours (Spring colours are good)
-I want the flyer to convey joy or happiness
-Use my photo which is attached as the predominant image (you can crop it to remove the background etc)

The Flyer Details are as follows:

Somewhere Past Tomorrow - Brisbane Tour

Join Author & Speaker, Rosalind Okafe, as she speaks about her new book entitled 'Somewhere Past Tomorrow'.

Be inspired and encouraged to embrace the life that God has given you and make the most of it!

Date: Saturday 9th November 2013
Time: 2:00 pm - 5:00 pm
Location: Larkwell Hotel Brisbane (Juniper Ballroom)
Fennimore Street, Brisbane QLD 4000
Tickets: $60/pp (Includes High Tea)
Buy Tickets: www.rosalindokafe.com or http://somewherepasttomorrow.ticketvane.net

Email: info@rosalindokafe.com

Include the cover of my new book.

www.rosalindokafe.com (include my website at the bottom of the flyer)

Target Market(s)

Young professional women aged between their mid 20's to late 30's

Industry/Entity Type

Event

Requirements
Should not have
• -No girly or curly font

```html
<!DOCTYPE html>
<html lang="en">
<head>
<meta charset="utf-8">
<title>Somewhere Past Tomorrow – Brisbane Seminar Flyer</title>
<link rel="stylesheet" href="https://fonts.googleapis.com/css2?family=Open+Sans:wdth,wght@75..100,300..800&display=swap">
<style>
  :root {
    --lavender: #cbc0e0;
    --ink: #111111;
    --cover-light: #f7f6f4;
    --cover-shade: #d9d6d2;
    --photo-dark: #2a211d;
    --photo-skin: #8a5a3c;
  }
  html, body {
    margin: 0;
    padding: 0;
    overflow: hidden;
    background: var(--lavender);
  }
  .flyer {
    position: relative;
    width: 927px;
    height: 1200px;
    background: var(--lavender);
    color: var(--ink);
    font-family: "Open Sans", sans-serif;
    font-stretch: 75%;
    overflow: hidden;
  }
  .intro {
    position: absolute;
    top: 114px;
    left: 0;
    width: 100%;
    text-align: center;
    font-size: 27px;
    font-weight: 400;
    margin: 0;
  }
  .speaker-name {
    position: absolute;
    left: 150px;
    top: 310px;
    width: 380px;
    text-align: center;
    margin: 0;
    font-size: 58px;
    font-weight: 400;
    letter-spacing: -1px;
    line-height: 1;
    white-space: nowrap;
    transform: rotate(-15deg);
    transform-origin: center;
  }
  .speaker-photo {
    position: absolute;
    left: 562px;
    top: 206px;
    width: 172px;
    height: 188px;
    background: radial-gradient(ellipse at 50% 38%, var(--photo-skin) 0%, var(--photo-skin) 26%, var(--photo-dark) 55%);
  }
  .lead-in {
    position: absolute;
    top: 472px;
    left: 0;
    width: 100%;
    text-align: center;
    margin: 0;
    font-size: 23px;
    font-weight: 400;
  }
  .book-title {
    position: absolute;
    top: 572px;
    left: 0;
    width: 100%;
    text-align: center;
    margin: 0;
    font-size: 80px;
    font-weight: 500;
    letter-spacing: -2px;
    line-height: 1;
    white-space: nowrap;
    text-transform: uppercase;
  }
  .book-cover {
    position: absolute;
    left: 78px;
    top: 728px;
    width: 270px;
    height: 318px;
    background: linear-gradient(100deg, var(--cover-shade) 0%, var(--cover-light) 18%, var(--cover-light) 80%, var(--cover-shade) 100%);
  }
  .event-details {
    position: absolute;
    left: 401px;
    top: 766px;
    margin: 0;
    padding: 0;
    list-style: none;
    font-size: 17px;
    font-stretch: 85%;
    line-height: 26.5px;
    white-space: nowrap;
  }
  .event-details .indent {
    display: block;
    padding-left: 125px;
  }
  .event-details .indent-wide {
    display: block;
    padding-left: 110px;
  }
  .website {
    position: absolute;
    right: 58px;
    top: 1128px;
    margin: 0;
    font-size: 34px;
    font-stretch: 85%;
    font-weight: 400;
  }
</style>
</head>
<body>
<main class="flyer">
  <p class="intro">Join Author and Speaker</p>
  <h2 class="speaker-name">ROSALIND OKAFE</h2>
  <div class="speaker-photo" role="img" aria-label="Portrait photo of the author, smiling, in a black leather jacket"></div>
  <p class="lead-in">as she speaks abount her new book entitled</p>
  <h1 class="book-title">“Somewhere Past Tomorrow”</h1>
  <div class="book-cover" role="img" aria-label="Cover of the book Somewhere Past Tomorrow by Rosalind Okafe, a woman in white between two men"></div>
  <ul class="event-details">
    <li>Date : Saturday, November 09, 2013</li>
    <li>Time : 2:00 p.m. to 5:00 p.m.</li>
    <li>Location : Larkwell Hotel Brisbane (Juniper Ballroom)
      <span class="indent">Fennimore Street, Brisbane QLD 4000</span></li>
    <li>Ticket price : $60/pp (Includes High Tea)</li>
    <li>Buy Ticket : www.rosalindokafe.com or
      <span class="indent-wide">http://somewherepasttomorrow.ticketvane.net</span></li>
    <li>Email : info@rosalindokafe.com</li>
  </ul>
  <p class="website">www.rosalindokafe.com</p>
</main>
</body>
</html>
```